Zielgruppe
Ich bin mit TK-Vorsorge als unabhängiger Versicherungsagent Selbstständig. (www.tk-vorsorge.de)
Ich habe mich auf die Absicherung von biometrischen Risiken spezialisiert - die auch in der Broschüre Thematisiert werden sollen. Das Oberthema der Broschüre ist 'biometrische Risiken'. Dies soll dann auf die Themen: Arbeitskraft, Langlebigkeit und Pflege heruntergebrochen werden.
Zielgruppe sind vor allem junge Menschen, die gerade erst eine Ausbildung gestartet oder ihr Studium beendet haben.
Aufgabenstellung
Das Design sollte die drei Hauptbereiche: Arbeitskraft, Langlebigkeit und Pflege, leicht verständlich dem Kunden veranschaulichen. Texte, Informationen und Grafiken (in der Reihenfolge, so wie ich mir das vorstelle) sind als Datei beigefügt.
Das ganze soll im DIN A4 Format gedruckt werden, wobei ich auf einen Hochwertigen Druck inklusive Druckveredelung hohen Wert lege.

```html
<!DOCTYPE html>
<html lang="de">
<head>
<meta charset="utf-8">
<title>TK-Vorsorge – Biometrische Risiken</title>
<link href="https://fonts.googleapis.com/css2?family=Open+Sans:ital,wght@0,300;0,400;0,600;0,700;1,700&display=swap" rel="stylesheet">
<style>
:root{
  --teal:#14a19a;
  --grey:#d9d9d9;
  --ink:#222;
  --soft:#8a8a8a;
  --white:#fff;
  --table:#dff1f6;
}
*{margin:0;padding:0;box-sizing:border-box}
html,body{width:1200px;height:2637px;overflow:hidden;background:var(--white)}
body{position:relative;font-family:"Open Sans",sans-serif;color:var(--ink)}
.page{position:absolute;background:var(--white);box-shadow:0 0 18px rgba(0,0,0,.35);overflow:hidden}
.page svg.shapes{position:absolute;left:0;top:0}
.cover{left:403px;top:157px;width:392px;height:550px}
.spread-a{left:212px;top:760px;width:773px;height:550px}
.spread-b{left:212px;top:1362px;width:773px;height:550px}
.back{left:403px;top:1963px;width:392px;height:550px}
.t{position:absolute;line-height:1.35}
.small{font-size:6.8px}
.tiny{font-size:6px}
.brand{display:flex;align-items:center;gap:6px;font-size:20px;font-weight:600;color:var(--ink)}
.brand .dot{width:34px;height:34px;border-radius:50%;background:var(--ink)}
.brand.on-teal{color:var(--ink)}
.ribbon{color:var(--white);font-weight:700;font-size:12px;transform-origin:left top;white-space:nowrap}
.quote{color:var(--white);font-weight:700;font-size:22px;line-height:1.32}
.section-title{font-size:11px;font-weight:600;line-height:1.2}
.section-sub{font-size:10px;line-height:1.2}
.rule{position:absolute;height:1px;background:var(--teal);opacity:.6}
.lead{font-size:19px;font-weight:300;color:var(--soft);line-height:1.25}
.accent{color:var(--teal)}
.strong{font-weight:700}
.figure{position:absolute;border-radius:3px}
.stat{position:absolute;width:62px;text-align:center;font-size:5.6px;color:var(--soft);line-height:1.25}
.stat b{display:block;font-size:8px;font-weight:600;color:var(--soft);margin-bottom:2px}
.badge{position:absolute;width:52px;height:52px;border-radius:50%;background:var(--teal);border:2px solid var(--white);color:var(--white);font-size:5px;font-weight:700;text-align:center;display:flex;align-items:flex-end;justify-content:center;padding-bottom:9px;line-height:1.1}
.gap-label{color:var(--white);font-weight:700;font-size:12.5px;line-height:1.25}
.cost-table{position:absolute;width:122px;height:62px;background:var(--table);padding:5px 5px 4px 16px;font-size:3.6px;line-height:1.45}
.cost-table .icon{position:absolute;left:3px;top:4px;width:9px;height:11px;border:1px solid #3a7d9a;border-radius:1px}
.cost-table .row{display:flex;justify-content:space-between}
.cost-table .total{margin-top:3px;font-weight:700}
.contact{color:var(--white);font-size:8px;line-height:20px}
</style>
</head>
<body>

<!-- Cover -->
<section class="page cover">
  <svg class="shapes" width="392" height="550" viewBox="0 0 392 550">
    <rect width="392" height="550" fill="var(--grey)"/>
    <polygon points="392,0 392,328 45,162" fill="var(--white)"/>
    <polygon points="330,0 392,0 40,163 12,160" fill="var(--teal)"/>
    <polygon points="0,162 392,342 135,550 0,550" fill="var(--teal)"/>
  </svg>
  <div class="t brand" style="left:33px;top:38px"><span class="dot"></span>TK-Vorsorge</div>
  <div class="t ribbon" style="left:110px;top:112px;transform:rotate(-24deg)">Biometrische Risiken</div>
  <div class="t strong" style="left:113px;top:149px;font-size:11.5px">Arbeitskraft • Langlebigkeit • Pflege</div>
  <div class="t" style="left:190px;top:169px;width:170px;font-size:7.6px">Viele Menschen sind bisher nur unzureichend über das große Potenzial dieser Risiken und vor allem ihrer existenzbedrohenden Folgen aufgeklärt.</div>
  <div class="t quote" style="left:22px;top:318px">" Welche Versicherungen<br>brauche ich denn wirklich? "</div>
  <div class="t tiny" style="left:22px;top:384px;color:var(--ink)">Wir sind Ihr Spezialist auf dem Gebiet der biometrischen Risikoabsicherung.</div>
  <div class="t" style="right:24px;top:480px;width:200px;text-align:right;font-size:7.4px;color:var(--ink)">Auf den nachfolgenden Seiten finden Sie einige Erläuterungen zu den wichtigsten Aspekten in der Absicherung von biometrischen Risiken.</div>
</section>

<!-- Arbeitskraft / Langlebigkeit -->
<section class="page spread-a">
  <svg class="shapes" width="773" height="550" viewBox="0 0 773 550">
    <polygon points="0,325 763,550 0,550" fill="var(--grey)"/>
    <polygon points="0,300 773,528 773,550 763,550 0,325" fill="var(--teal)"/>
    <polygon points="600,228 773,128 773,310" fill="var(--teal)"/>
    <path d="M632 227 h34 M660 222 l6 5 l-6 5" stroke="var(--white)" stroke-width="1.2" fill="none"/>
    <path d="M175 84 h20 M190 80 l5 4 l-5 4" stroke="var(--ink)" stroke-width=".9" fill="none"/>
    <path d="M560 350 h20 M575 346 l5 4 l-5 4" stroke="var(--ink)" stroke-width=".9" fill="none"/>
  </svg>
  <div class="rule" style="left:8px;top:50px;width:757px"></div>

  <div class="t section-title" style="left:22px;top:18px">Arbeitskraft</div>
  <div class="t section-sub" style="left:22px;top:32px">„Haben Sie ohne Arbeitskraft noch ein Einkommen?“</div>
  <div class="t small" style="left:22px;top:58px;width:145px">Wer aus gesundheitlichen Gründen nicht mehr in der Lage ist, zu arbeiten, wird vom Staat durch die Volle bzw. Halbe Erwerbsminderungsrente aufgefangen. Ob halbe oder Volle Erwerbsminderungsrente entscheidet sich anhand der verbliebenen Rest Erwerbsfähigkeit.</div>
  <div class="t small" style="left:213px;top:58px;width:150px">Der bisherige Beruf sowie die Arbeitsmarktlage bleiben hierbei grundsätzlich unberücksichtigt. Sie werden also ohne Rücksicht auf Status, Qualifikation und Zumutbarkeit auf irgendeine Tätigkeit des Allgemeinen Arbeitsmarktes hingewiesen.</div>
  <div class="t small" style="left:22px;top:146px;width:135px">Einer von 4 Menschen kann im Laufe seines Lebens, einen ursprünglichen Beruf aus gesund heitlichen Gründen nicht mehr ausüben!</div>
  <div class="figure" role="img" aria-label="Personensymbol" style="left:33px;top:185px;width:12px;height:40px;background:var(--soft)"></div>
  <div class="figure" role="img" aria-label="Personensymbol" style="left:66px;top:185px;width:12px;height:40px;background:var(--soft)"></div>
  <div class="figure" role="img" aria-label="Personensymbol, hervorgehoben" style="left:99px;top:185px;width:12px;height:40px;background:var(--teal)"></div>
  <div class="figure" role="img" aria-label="Personensymbol" style="left:132px;top:185px;width:12px;height:40px;background:var(--soft)"></div>
  <div class="t small accent" style="left:22px;top:236px;width:100px">Können Sie wissen ob Sie einer der anderen drei oder der EINE sind?</div>

  <div class="t strong" style="left:213px;top:143px;width:140px;font-size:7.8px;line-height:1.2">Welchen physischen oder psychischen Belastungen sind Sie ausgesetzt?</div>
  <div class="figure" role="img" aria-label="Symbol: Bewegungsapparat" style="left:226px;top:178px;width:20px;height:40px;background:var(--soft)"></div>
  <div class="figure" role="img" aria-label="Symbol: Herz und Gefäße" style="left:282px;top:178px;width:12px;height:40px;background:var(--soft)"></div>
  <div class="figure" role="img" aria-label="Symbol: Krebserkrankung" style="left:334px;top:178px;width:12px;height:40px;background:var(--soft)"></div>
  <div class="stat" style="left:205px;top:232px"><b>21 %</b>Erkrankungen des Skelett und Bewegungsapparates</div>
  <div class="stat" style="left:257px;top:232px"><b>7 %</b>Erkrankungen des Herzens und des Gefäßsystems</div>
  <div class="stat" style="left:309px;top:232px"><b>15%</b>Krebs und andere bösartige Geschwülste</div>
  <div class="figure" role="img" aria-label="Symbol: Psyche" style="left:230px;top:282px;width:12px;height:44px;background:var(--soft)"></div>
  <div class="figure" role="img" aria-label="Symbol: Unfall" style="left:276px;top:290px;width:26px;height:34px;background:var(--soft)"></div>
  <div class="figure" role="img" aria-label="Symbol: Sonstige Erkrankungen" style="left:327px;top:282px;width:30px;height:30px;border-radius:50%;background:var(--teal)"></div>
  <div class="stat" style="left:205px;top:340px"><b>32 %</b>Nerven und Psychische Erkrankungen</div>
  <div class="stat" style="left:257px;top:340px"><b>9 %</b>Unfälle</div>
  <div class="stat" style="left:309px;top:340px"><b>16 %</b>Sonstige Erkrankungen</div>

  <div class="t ribbon" style="left:56px;top:322px;transform:rotate(16.5deg);font-style:italic;font-size:12.5px">Ihr größtes Vermögen ist Ihre Arbeitskraft.</div>
  <div class="t strong" style="left:22px;top:404px;font-size:7.6px;font-weight:600">Lösungen der Absicherung Ihrer Arbeitskraft</div>
  <div class="badge" style="left:22px;top:422px">Berufs-<br>unfähigkeits-<br>schutz</div>
  <div class="badge" style="left:117px;top:422px">Grundfähigkeits-<br>absicherungen</div>
  <div class="badge" style="left:212px;top:422px">Schwere<br>Krankheiten<br>Vorsorge</div>
  <div class="t" style="left:22px;top:488px;font-size:7.4px">Wir haben uns auf die Absicherung der Arbeitskraft spezialisiert.<br>Lassen Sie sich von uns ein individuelles Vorsorgekonzept erarbeiten.</div>

  <div class="t section-title" style="left:403px;top:18px">Langlebigkeit</div>
  <div class="t section-sub" style="left:403px;top:32px">„Können Sie ihr tägliches Leben noch selbst bewältigen?“</div>
  <div class="t small" style="left:405px;top:58px;width:150px">Da die Renten im Vergleich zu den Löhnen künftig geringer steigen werden und sich somit die spätere Lücke zwischen Rente und Erwerbseinkommen vergrößert, wird eine zusätzliche Absicherung für das Alter wichtiger („Versorgungslücke“).</div>
  <div class="t lead" style="left:404px;top:128px">Reicht Ihnen<br>Ihre gesetzliche Rente?</div>
  <div class="t small" style="left:404px;top:186px;width:190px;font-size:6.4px">
    <span class="strong">Renteninformation</span><br>
    Rentenhöhe bei Renteneintritt &nbsp;&nbsp; <span class="strong">1.700 € Brutto</span><br>
    10% Beitrag Kranken- &amp; Pflegeversicherung<br>
    15% Abzüge Einkommenssteuer<br><br>
    <span class="strong">Netto Rente</span> &nbsp;&nbsp;&nbsp;&nbsp;&nbsp;&nbsp;&nbsp;&nbsp;&nbsp;&nbsp;&nbsp;&nbsp;&nbsp;&nbsp;&nbsp;&nbsp;&nbsp;&nbsp;&nbsp;&nbsp;&nbsp;&nbsp; <span class="strong">1.275 € Netto</span><br>
    Inflation von 1,5% jährlich<br>
    87% Kaufkraft nach 10 Jahren 1.110 € tatsächlich<br>
    75% Kaufkraft nach 20 Jahren 956 € tatsächlich
  </div>
  <div class="t gap-label" style="left:664px;top:205px">Lücke von<br>800 €/mtl.</div>
  <div class="t lead" style="left:404px;top:298px">Hier ist Eigenverantwortung gefragt!</div>
  <div class="t small" style="left:405px;top:336px;width:140px;font-size:6.4px">Die Zahlung einer lebenslangen Rente ist die einzige Möglichkeit das Langlebigkeitsrisiko abzusichern.</div>
  <div class="t small" style="left:590px;top:336px;width:150px;font-size:6.4px">Andere Produkte leisten das nicht: Investmentprodukte mit Auszahlungsplan oder Sparguthaben zum Beispiel, enden zu einem bestimmten Zeitpunkt</div>
  <div class="t" style="left:405px;top:404px;width:310px;font-size:7.4px">Wir arbeiten zusammen mit Ihnen ein individuelles Vorsorgekonzept aus, um die richtigen Weichen so früh wie möglich zu stellen.</div>
</section>

<!-- Pflege / Leistungsversprechen -->
<section class="page spread-b">
  <svg class="shapes" width="773" height="550" viewBox="0 0 773 550">
    <defs>
      <linearGradient id="walkTones" x1="0" y1="0" x2="1" y2="1">
        <stop offset="0" stop-color="#6b5a3c"/>
        <stop offset=".55" stop-color="#c9a45c"/>
        <stop offset="1" stop-color="#e8d39a"/>
      </linearGradient>
    </defs>
    <polygon points="386,0 773,0 773,4 386,198" fill="url(#walkTones)" role="img" aria-label="Foto: Nahaufnahme laufender Schuhe auf einem Weg bei Sonnenuntergang"/>
    <polygon points="490,150 773,6 773,20 510,156" fill="var(--teal)"/>
    <polygon points="218,288 383,200 383,392" fill="var(--teal)"/>
    <polygon points="386,405 386,550 568,550" fill="var(--grey)"/>
    <polygon points="386,385 600,550 575,550 386,405" fill="var(--teal)"/>
  </svg>
  <div class="rule" style="left:8px;top:50px;width:372px"></div>
  <div class="t section-title" style="left:20px;top:20px">Pflege</div>
  <div class="t section-sub" style="left:20px;top:34px">„Können Sie sich alt werden auch finanziell leisten?“</div>
  <div class="t small" style="left:20px;top:57px;width:185px">Die Menschen in Deutschland werden immer älter. Das ist schön. Doch Sie werden auch immer pflegebedürftiger. Das ist weniger schön und macht Private Vorsorge notwendiger denn je.</div>

  <div class="cost-table" style="left:22px;top:112px">
    <span class="icon"></span>
    <div class="strong">Beispiel: Monatlicher Eigenanteil im Pflegegrad 3</div>
    <div class="row"><span>Eigenanteil Pflegeheim</span><span>1.090 €</span></div>
    <div class="row"><span>Unterkunft und Verpflegung</span><span>695 €</span></div>
    <div class="row"><span>Investitionskosten</span><span>387 €</span></div>
    <div class="row total"><span>Eigenanteil</span><span>2.172 €</span></div>
    <div class="row total"><span>Eigenanteil nach 7 Jahren</span><span>182.448 €</span></div>
  </div>
  <div class="cost-table" style="left:150px;top:112px">
    <span class="icon"></span>
    <div class="strong">Beispiel: Monatlicher Eigenanteil im Pflegegrad 5</div>
    <div class="row"><span>Eigenanteil Pflegeheim</span><span>540 €</span></div>
    <div class="row"><span>Unterkunft und Verpflegung</span><span>695 €</span></div>
    <div class="row"><span>Investitionskosten</span><span>387 €</span></div>
    <div class="row total"><span>Eigenanteil</span><span>1.622 €</span></div>
    <div class="row total"><span>Eigenanteil nach 7 Jahren</span><span>136.248 €</span></div>
  </div>
  <div class="t" style="left:84px;top:186px;font-size:8.4px">Können Sie sich das leisten?</div>
  <div class="t small" style="left:20px;top:212px;width:245px">Die Kosten für Pflege sind einzig und allein von einer Frage abhängig: Wie und auf welchem Niveau möchten Sie persönlich gepflegt und betreut werden?</div>
  <div class="t small" style="left:20px;top:256px;width:210px">Wer auf die Risiken eines Pflegefalls nicht vorbereitet ist, gerät schnell in eine finanzielle Schieflage.</div>
  <div class="t lead" style="left:21px;top:287px;font-size:20px">Pflegebedürftigkeit…<br>es kann jeden treffen!</div>
  <div class="t small" style="left:20px;top:346px">Staatliche Versorgung - Teilkasko im Pflegefall</div>
  <div class="t small" style="left:20px;top:362px;width:255px">1995 wurde vom Gesetzgeber die staatliche Pflegepflichtversicherung ins Leben gerufen. 2017 fand dazu eine grundlegende Reform statt, unter anderem wurde die Pflegebedürftigkeit mit fünf Pflegegraden neu definiert. Der Pflegegrad ergibt sich aus einem Punktesystem und basiert auf sechs relevante Kategorien.</div>
  <div class="t lead" style="left:21px;top:408px;font-size:20px">Eines bleibt aber gleich:</div>
  <div class="t small" style="left:20px;top:446px;width:180px">Die gesetzliche Pflegeversicherung sorgt weiterhin NUR für die minimale Grundsicherung</div>
  <div class="t" style="left:20px;top:485px;width:260px;font-size:7.4px">Wir helfen Ihnen dabei gezielt diese Lücken zu schließen indem wir mit Ihnen ein individuelles Vorsorgekonzept ausarbeiten.</div>
  <div class="t strong" style="right:402px;top:258px;width:130px;text-align:right;color:var(--white);font-size:7.6px;line-height:1.3;font-weight:600">25 Menschen<br><span style="font-weight:400">unter 65 Jahren, werden in Deutschland jeden Tag zum Pflegefall, beispielsweise durch Unfälle oder Krankheiten.</span></div>

  <div class="t lead" style="left:418px;top:192px;font-size:20px">Wir stehen für:<br>TOP Bedingungen<br>den besten Versicherungsschutz</div>
  <div class="t small" style="left:418px;top:283px;width:265px">Die meisten Menschen sind sich der herrschenden Probleme der fehlenden Absicherung der Arbeitskraft, der Altersarmut und des Pflegenotstands sehr wohl bewusst. Allerdings mangelt es noch an Handlungen.</div>
  <div class="t small" style="left:418px;top:319px;width:265px">Dies liegt sehr oft daran, dass der Ansprechpartner/Problemlöser in diesem Bereich fehlt.</div>
  <div class="t small" style="left:418px;top:346px;width:265px">Genau da stellen wir uns auf!<br>Es ist Aufgabe des Vermittlers, Angaben in den Bedingungen &amp; den Tarifen zu überprüfen und zu gewichten.</div>
</section>

<!-- Back -->
<section class="page back">
  <svg class="shapes" width="392" height="550" viewBox="0 0 392 550">
    <polygon points="0,0 392,0 392,160" fill="var(--grey)"/>
    <polygon points="10,0 50,0 392,155 392,180" fill="var(--teal)"/>
    <polygon points="0,335 392,165 392,550 250,550" fill="var(--teal)"/>
    <polygon points="0,340 0,550 250,550" fill="var(--grey)"/>
  </svg>
  <div class="t" style="left:38px;top:148px;font-size:7.4px;line-height:1.35">Du hast Fragen zu meiner Arbeit?<br>Oder Unklarheiten zu einer bestimmten Versicherung?<br>Melde dich bei mir!</div>
  <div class="t brand on-teal" style="left:186px;top:345px"><span class="dot"></span>TK-Vorsorge</div>
  <div class="t contact" style="left:226px;top:382px">
    Worbis Malte<br>
    Lindenweg 4<br>
    86150 Augsburg<br>
    Telefon: 0821 5504218<br>
    Mobil: 0176 20481937<br>
    E-Mail: malte.worbis@tk-vorsorge.de
  </div>
</section>

</body>
</html>
```